Business Cards

Need a neat design for a new business card

Industry/Entity Type

Residential Construction

Contact Information for Business Card

Company Name- KORV Construction Inc.
Owner- Daniel Pruitt
Phone number- (555)270-4418
Email- korvcobuilds@mailbox-example.com
Facebook- www.socialpage-example.com/korvcobuilds

Colors
fefdec

```html
<!DOCTYPE html>
<html lang="en">
<head>
<meta charset="utf-8">
<title>KORV Construction Inc. – Business Card</title>
<link href="https://fonts.googleapis.com/css2?family=Poppins:wght@300;400;500;600&display=swap" rel="stylesheet">
<style>
  :root {
    --stage: #2a2a2d;
    --card: #1c1d1f;
    --ink: #fefdec;
    --ink-soft: #d9d8c8;
  }
  * { margin: 0; padding: 0; box-sizing: border-box; }
  html, body { width: 1200px; height: 800px; overflow: hidden; }
  body {
    background: var(--stage);
    font-family: 'Poppins', sans-serif;
    color: var(--ink);
    display: flex;
    flex-direction: column;
    align-items: center;
    justify-content: center;
    gap: 56px;
  }
  .card {
    position: relative;
    width: 540px;
    height: 309px;
    background: var(--card);
    border-radius: 3px;
    box-shadow: 0 10px 30px rgba(0,0,0,0.45);
    overflow: hidden;
  }

  /* brand lockup */
  .brand {
    display: flex;
    flex-direction: column;
    align-items: center;
    gap: 6px;
  }
  .brand-row { display: flex; align-items: center; gap: 10px; }
  .brand-mark { width: 14px; height: 14px; background: var(--ink); }
  .brand-name {
    font-weight: 500;
    font-size: 44px;
    letter-spacing: 4px;
    line-height: 1;
  }
  .brand-sub {
    font-weight: 400;
    font-size: 12px;
    letter-spacing: 3.5px;
    text-transform: uppercase;
  }

  .card--front { display: flex; align-items: center; justify-content: center; }

  /* back */
  .card--back .brand {
    position: absolute;
    left: 34px;
    top: 112px;
    width: 180px;
  }
  .card--back .brand-name { font-size: 36px; letter-spacing: 3px; }
  .card--back .brand-sub { font-size: 10px; letter-spacing: 3px; }

  .divider {
    position: absolute;
    left: 232px;
    top: 62px;
    width: 1px;
    height: 140px;
    background: var(--ink);
  }
  .person {
    position: absolute;
    left: 252px;
    top: 58px;
  }
  .person-name {
    font-weight: 600;
    font-size: 18px;
    letter-spacing: 0.5px;
    text-transform: uppercase;
    line-height: 1.1;
  }
  .person-role { font-size: 10px; font-weight: 400; color: var(--ink-soft); }

  .contacts {
    position: absolute;
    left: 252px;
    top: 130px;
    list-style: none;
    display: flex;
    flex-direction: column;
    gap: 6px;
  }
  .contact {
    display: flex;
    align-items: center;
    gap: 8px;
    font-size: 10px;
    font-weight: 300;
    white-space: nowrap;
  }
  .contact-icon { width: 11px; height: 11px; flex: none; }
  .contact-dot {
    width: 8px; height: 8px; margin: 0 1.5px;
    border-radius: 50%; background: var(--ink); flex: none;
  }

  .baseline {
    position: absolute;
    left: 0;
    top: 262px;
    width: 330px;
    height: 2px;
    background: var(--ink);
  }
  .company {
    position: absolute;
    left: 344px;
    top: 254px;
    font-size: 11px;
    font-weight: 500;
    letter-spacing: 0.4px;
    text-transform: uppercase;
  }
</style>
</head>
<body>

  <section class="card card--front" aria-label="Card front">
    <div class="brand">
      <div class="brand-row">
        <span class="brand-mark"></span>
        <span class="brand-name">KORV</span>
      </div>
      <span class="brand-sub">Construction</span>
    </div>
  </section>

  <section class="card card--back" aria-label="Card back">
    <div class="brand">
      <div class="brand-row">
        <span class="brand-mark"></span>
        <span class="brand-name">KORV</span>
      </div>
      <span class="brand-sub">Construction</span>
    </div>

    <div class="divider"></div>

    <div class="person">
      <p class="person-name">Daniel Pruitt</p>
      <p class="person-role">CEO</p>
    </div>

    <ul class="contacts">
      <li class="contact">
        <svg class="contact-icon" viewBox="0 0 12 12" aria-hidden="true">
          <rect x="3" y="0.8" width="6" height="10.4" rx="1" fill="none" stroke="#fefdec" stroke-width="1.2"/>
          <line x1="5.2" y1="9.4" x2="6.8" y2="9.4" stroke="#fefdec" stroke-width="1"/>
        </svg>
        (555)270-4418
      </li>
      <li class="contact">
        <svg class="contact-icon" viewBox="0 0 12 12" aria-hidden="true">
          <rect x="0.6" y="2.2" width="10.8" height="7.6" fill="#fefdec"/>
          <polyline points="0.6,2.4 6,6.6 11.4,2.4" fill="none" stroke="#1c1d1f" stroke-width="1"/>
        </svg>
        korvcobuilds@mailbox-example.com
      </li>
      <li class="contact">
        <span class="contact-dot"></span>
        www.socialpage-example.com/korvcobuilds
      </li>
    </ul>

    <div class="baseline"></div>
    <p class="company">KORV Construction Inc.</p>
  </section>

</body>
</html>
```